Website Design For Stitchcraftparlour.com

What: A range of Tapestry Kits, books & Accessories.
Who: Appeals to ladies 45-70 years.

What we need:
A home page and template for a product page
The home page needs to include the image and something we can use as a logo to get started.

Image:
I love the 'Maud Pellingham' feel, hearts, flags and bunting.
Tapestry tends to be rich, heavy fabrics so dark burgendy reds and navy blues might work quite well in moderation.

Layout:
I would like the core structure of the site to be similar to:
http://www.fernyplumes.co.uk (although this is just a suggestion feel free to try something else if you think it might work better.
Buttons along the top: Home, About Tapestry, Delivery, Contact Us (the drop down on Our Range is Tapestry Cushions.

I would also like the search box to be a little bigger and can be relocated.

Tabs under the image
Cushion Kits, Hanging Tapestrys, Books, Accessories, Advice
Then an area for featured products under that.

Images - You can use any of the images from The Vintage Linenwork Company - tapestry section to build a feel for how the site might look when populated with product.

Female 45-75yrs -

• Build with SEO in mind.
Some space for text on home page for seo
Some images below to give a feel for styling

```html
<!DOCTYPE html>
<html lang="en">
<head>
<meta charset="utf-8">
<title>Stitchcraft Parlour – Union Jack Heart Tapestry</title>
<link rel="stylesheet" href="https://fonts.googleapis.com/css2?family=Arimo:ital,wght@0,400;0,700;1,700&family=Dancing+Script:wght@500&display=swap">
<style>
  :root {
    --navy: #1b3c6e;
    --navy-text: #163a70;
    --heading-blue: #1f4f88;
    --red: #c3242a;
    --red-dark: #9b1a1f;
    --burgundy: #8c1f2a;
    --green-top: #7fd12a;
    --green-bottom: #3f9710;
    --nav-top: #c3cfdc;
    --nav-bottom: #9eb0c4;
    --line-grey: #dcdcdc;
    --border-grey: #b9b9b9;
    --text: #222;
    --muted: #7a7a7a;
    --page-bg: #ffffff;
  }
  * { box-sizing: border-box; margin: 0; padding: 0; }
  html, body {
    width: 1117px; height: 1200px; overflow: hidden;
    background: var(--page-bg);
    font-family: "Arimo", Arial, sans-serif; color: var(--text);
  }
  .canvas { position: relative; width: 1117px; height: 1200px; }
  .abs { position: absolute; }

  /* Header */
  .brand { left: 40px; top: 88px; display: flex; align-items: center; gap: 12px; }
  .brand-mark { width: 30px; height: 30px; background: var(--burgundy); }
  .brand-name { font-size: 36px; font-weight: 400; color: var(--navy); letter-spacing: .5px; }
  .tagline {
    left: 128px; top: 145px; font-family: "Dancing Script", cursive;
    font-size: 15px; color: var(--navy);
  }
  .search { left: 566px; top: 31px; display: flex; gap: 4px; }
  .search-field {
    width: 257px; height: 25px; border: 1px solid #9a9a9a;
    box-shadow: inset 0 1px 2px rgba(0,0,0,.25);
    font-size: 15px; color: #9a9a9a; padding: 3px 10px;
  }
  .search-button { width: 28px; height: 25px; background: var(--red-dark); display: flex; align-items: center; justify-content: center; }
  .account-links { left: 891px; top: 40px; font-size: 12px; color: var(--navy-text); display: flex; align-items: center; gap: 8px; }
  .account-links .sep { width: 2px; height: 17px; background: var(--navy); }
  .header-rule { left: 518px; top: 69px; width: 554px; height: 5px; background: var(--line-grey); }
  .help-bar {
    left: 637px; top: 76px; width: 435px; height: 63px;
    background: linear-gradient(#d3393c, var(--red) 60%, #b11e24);
    border: 1px solid #8e1519; box-shadow: 0 1px 2px rgba(0,0,0,.3);
    display: flex; align-items: center; padding-left: 22px; color: #fff;
  }
  .help-label {
    font-family: "Dancing Script", cursive; font-size: 22px;
    border-bottom: 1px solid rgba(255,255,255,.8); margin-left: 6px; line-height: 1.05;
  }
  .help-number { font-size: 24px; font-weight: 700; margin-left: 22px; letter-spacing: .3px; }

  /* Page panel */
  .panel {
    left: 36px; top: 177px; width: 1037px; height: 1010px; background: #fff;
    box-shadow: 0 0 3px rgba(0,0,0,.35);
  }
  .main-nav {
    left: 36px; top: 177px; width: 1037px; height: 39px;
    background: linear-gradient(var(--nav-top), var(--nav-bottom));
    display: flex; justify-content: flex-end; align-items: center; gap: 24px; padding-right: 53px;
    font-size: 14px; color: var(--navy-text);
  }

  /* Product */
  .product-photo {
    left: 75px; top: 241px; width: 395px; height: 397px; border: 1px solid var(--border-grey); padding: 2px;
  }
  .photo-fill { width: 100%; height: 100%; }
  .hero-fill { background: linear-gradient(120deg, #7a1e24 0%, #8b98b3 45%, #9ea9bf 60%, #6e5446 100%); }
  .thumb { left: 482px; width: 80px; border: 1px solid var(--border-grey); padding: 3px; }
  .thumb-one { top: 241px; height: 86px; }
  .thumb-two { top: 337px; height: 87px; }
  .thumb-fill { background: linear-gradient(135deg, #7c2028, #8e9ab3 60%, #5e4b40); }

  .product-info { left: 600px; top: 241px; width: 429px; height: 397px; border: 1px solid var(--border-grey); }
  .product-title { left: 630px; top: 257px; font-size: 20px; font-weight: 400; color: #111; }
  .product-sku { left: 633px; top: 286px; font-size: 12px; color: var(--muted); }
  .product-price { left: 633px; top: 333px; font-size: 32px; color: #111; }
  .qty-label { left: 793px; top: 318px; font-size: 12px; font-weight: 700; color: #333; }
  .qty-field {
    left: 794px; top: 337px; width: 28px; height: 24px; border: 1px solid #999;
    font-size: 12px; font-weight: 700; text-align: center; line-height: 22px;
  }
  .button-green {
    background: linear-gradient(var(--green-top), var(--green-bottom));
    color: #fff; font-weight: 700; text-align: center; border-radius: 14px;
    box-shadow: 0 1px 2px rgba(0,0,0,.35);
  }
  .add-to-basket { left: 832px; top: 332px; width: 127px; height: 34px; line-height: 32px; font-size: 15px; border-radius: 17px; }
  .info-rule { left: 630px; top: 384px; width: 337px; height: 4px; background: #a9a9a9; border-radius: 2px; }
  .info-heading { left: 633px; top: 422px; font-size: 13px; font-weight: 700; }
  .info-size { left: 633px; top: 453px; font-size: 13px; }
  .info-copy { left: 633px; top: 483px; width: 280px; font-size: 13px; line-height: 15.5px; }
  .like-button {
    left: 638px; top: 579px; width: 53px; height: 28px; border: 1px solid #c3c8d4; border-radius: 3px;
    background: linear-gradient(#f7f8fa, #e4e7ee); font-size: 11px; color: #3b5285;
    display: flex; align-items: center; justify-content: center; gap: 4px;
  }
  .like-button .dot { width: 9px; height: 9px; background: #5a6f9c; }

  /* Recommended */
  .section-heading { left: 77px; top: 697px; font-size: 20px; font-weight: 400; color: var(--heading-blue); }
  .product-row { left: 75px; top: 728px; display: flex; gap: 12px; }
  .product-card {
    width: 185px; height: 211px; border: 1px solid var(--border-grey);
    display: flex; flex-direction: column; align-items: center;
  }
  .card-photo {
    margin-top: 36px; width: 120px; height: 89px; border-radius: 8px;
    background: linear-gradient(135deg, #2f4a78 0%, #e9dfc9 30%, #b72c35 50%, #e9dfc9 70%, #2f4a78 100%);
  }
  .card-name { margin-top: 21px; font-size: 11px; color: #111; }
  .card-price { margin-top: 11px; font-size: 11px; color: #111; }
  .view-now { margin-top: 7px; width: 81px; height: 19px; line-height: 19px; font-size: 11px; border-radius: 10px; }

  /* Footer */
  .footer-rule { left: 60px; top: 1100px; width: 985px; height: 5px; background: var(--line-grey); }
  .footer-links { left: 64px; top: 1128px; font-size: 11px; display: flex; gap: 28px; }
  .footer-links .legal { display: flex; gap: 18px; }
  .payment { left: 745px; top: 1126px; display: flex; align-items: center; gap: 10px; }
  .payment-label { font-size: 12px; font-weight: 700; font-style: italic; color: var(--navy-text); }
  .payment-cards { display: flex; gap: 2px; }
  .card-badge { width: 32px; height: 21px; border: 1px solid #999; }
  .badge-red { background: #c4332d; }
  .badge-blue { background: #2b4a9b; }
  .badge-sky { background: #5f93cf; }
  .badge-light { background: #e6e8ee; }
  .badge-orange { background: #d6461f; }
</style>
</head>
<body>
<div class="canvas">

  <header>
    <div class="abs brand">
      <span class="brand-mark"></span>
      <span class="brand-name">Stitchcraft Parlour</span>
    </div>
    <p class="abs tagline">the best tapestry in the world</p>

    <form class="abs search" role="search">
      <div class="search-field">Search here</div>
      <div class="search-button">
        <svg width="18" height="18" viewBox="0 0 18 18" aria-hidden="true">
          <circle cx="11" cy="7" r="4.5" fill="none" stroke="#fff" stroke-width="2"/>
          <line x1="8" y1="10" x2="3" y2="15" stroke="#fff" stroke-width="3" stroke-linecap="round"/>
        </svg>
      </div>
    </form>

    <nav class="abs account-links">
      <span>View Basket</span><span class="sep"></span><span>My Account</span>
    </nav>
    <div class="abs header-rule"></div>

    <div class="abs help-bar">
      <svg width="16" height="24" viewBox="0 0 16 24" aria-hidden="true">
        <path d="M4 2 C1 4 0 8 2 14 C4 19 7 22 11 22 L13 18 L9 15 L7 16 C5 13 4 10 5 7 L7 6 L7 2 Z" fill="#fff"/>
      </svg>
      <span class="help-label">Need help? talk to us</span>
      <span class="help-number">01632 960418</span>
    </div>
  </header>

  <div class="abs panel"></div>
  <nav class="abs main-nav">
    <span>Home</span><span>About Tapestry</span><span>Our Range</span><span>Delivery</span><span>Contact Us</span>
  </nav>

  <main>
    <div class="abs product-photo">
      <div class="photo-fill hero-fill" role="img" aria-label="Photo of the Union Jack heart tapestry cushion on a leather sofa"></div>
    </div>
    <div class="abs thumb thumb-one">
      <div class="photo-fill thumb-fill" role="img" aria-label="Thumbnail of the heart cushion"></div>
    </div>
    <div class="abs thumb thumb-two">
      <div class="photo-fill thumb-fill" role="img" aria-label="Close-up thumbnail of the tapestry stitching"></div>
    </div>

    <section class="abs product-info" aria-label="Product details"></section>
    <h1 class="abs product-title">Union Jack Heart Tapestry</h1>
    <p class="abs product-sku">UJH1319</p>
    <p class="abs product-price">£45.00</p>
    <span class="abs qty-label">QTY</span>
    <div class="abs qty-field">1</div>
    <div class="abs button-green add-to-basket">Add to Basket</div>
    <div class="abs info-rule"></div>
    <h2 class="abs info-heading">Product Information:</h2>
    <p class="abs info-size">Size: 35cm x 35cm</p>
    <p class="abs info-copy">Lorem ipsum dolor sit amet, consectetur adipi-scing elit. Fusce sed mi at arcu tristique posu-ere eu nec orci. Sed ut erat mollis sem ultrices hendrerit. Vivamus id mauris at nisl aliquet lacinia imperdiet at neque.</p>
    <div class="abs like-button"><span class="dot"></span>Like</div>

    <h2 class="abs section-heading">Recommended Products</h2>
    <div class="abs product-row">
      <article class="product-card">
        <div class="card-photo" role="img" aria-label="Union Jack rectangular cushion"></div>
        <p class="card-name">Union Jack Rectangular Cushion</p>
        <p class="card-price">£45.00</p>
        <div class="button-green view-now">View Now</div>
      </article>
      <article class="product-card">
        <div class="card-photo" role="img" aria-label="Union Jack rectangular cushion"></div>
        <p class="card-name">Union Jack Rectangular Cushion</p>
        <p class="card-price">£45.00</p>
        <div class="button-green view-now">View Now</div>
      </article>
      <article class="product-card">
        <div class="card-photo" role="img" aria-label="Union Jack rectangular cushion"></div>
        <p class="card-name">Union Jack Rectangular Cushion</p>
        <p class="card-price">£45.00</p>
        <div class="button-green view-now">View Now</div>
      </article>
      <article class="product-card">
        <div class="card-photo" role="img" aria-label="Union Jack rectangular cushion"></div>
        <p class="card-name">Union Jack Rectangular Cushion</p>
        <p class="card-price">£45.00</p>
        <div class="button-green view-now">View Now</div>
      </article>
      <article class="product-card">
        <div class="card-photo" role="img" aria-label="Union Jack rectangular cushion"></div>
        <p class="card-name">Union Jack Rectangular Cushion</p>
        <p class="card-price">£45.00</p>
        <div class="button-green view-now">View Now</div>
      </article>
    </div>
  </main>

  <footer>
    <div class="abs footer-rule"></div>
    <div class="abs footer-links">
      <span>© 2012 Stitchcraft Parlour</span>
      <span class="legal"><span>Terms and Conditions</span><span>Privacy Policy</span></span>
    </div>
    <div class="abs payment">
      <span class="payment-label">PAYMENT OPTIONS</span>
      <div class="payment-cards" aria-label="Accepted payment methods">
        <span class="card-badge badge-red"></span>
        <span class="card-badge badge-blue"></span>
        <span class="card-badge badge-sky"></span>
        <span class="card-badge badge-light"></span>
        <span class="card-badge badge-orange"></span>
      </div>
    </div>
  </footer>

</div>
</body>
</html>
```